Business Card Makeover. Recreate a sleek modern design for our business card.

DO NOT COPY OUR CURRENT DESIGN. MUST BE ONE SIDED BUSINESS CARD.
Create a new business card design, using our new logo. Attached is a sample of our current design and new logo. Please note the address and email will change. The new address is 417 Corvell West Palm Beach 33472 and our website will be www.talvendrake.example.

We are an architectural and interior design firm. We prefer a clean modern look. Something that is refined and emulates excellence.

Industry/Entity Type

Architecture

Contact Information for Business Card

clean modern look, please do not copy our attached design.

Font styles to use
Other font styles liked:
• see attached business card font

Colors

Designer to choose colors to be used in the design.

Requirements
Must have
• Must have a modern appeal and resemble our current branding.
Nice to have
• modern font, our logo, legible name and titles progressive design
Should not have
• Do not add colors not reflected in our branding. Should not look like our current card.

```html
<!DOCTYPE html>
<html lang="en">
<head>
<meta charset="utf-8">
<title>Talvendrake Business Card</title>
<link rel="stylesheet" href="https://fonts.googleapis.com/css2?family=Questrial&display=swap">
<style>
  :root {
    --page: #e9e7e3;
    --card: #ffffff;
    --blue-light: #22a9e0;
    --blue-deep: #0a78bb;
    --ink: #2c2c2c;
    --ink-soft: #5b5b5b;
    --white: #ffffff;
  }
  html, body {
    margin: 0;
    padding: 0;
    width: 1200px;
    height: 780px;
    overflow: hidden;
    background: var(--page);
  }
  .canvas {
    position: relative;
    width: 1200px;
    height: 780px;
  }
  .business-card {
    position: absolute;
    left: 150px;
    top: 133px;
    width: 900px;
    height: 514px;
    background: var(--card);
    box-shadow: 0 14px 40px rgba(0, 0, 0, 0.18);
    overflow: hidden;
  }
  .business-card svg {
    display: block;
    font-family: "Questrial", sans-serif;
  }
  .company-name { fill: var(--ink-soft); font-size: 44px; letter-spacing: 1px; }
  .logo-dot { fill: var(--blue-deep); }
  .address { fill: var(--ink); font-size: 18px; }
  .contact { fill: var(--ink); font-size: 17px; letter-spacing: 0.5px; }
  .license { fill: var(--ink); font-size: 15px; letter-spacing: 0.5px; }
  .icon-bg { fill: var(--blue-light); }
  .icon-glyph { fill: none; stroke: var(--white); stroke-width: 1.3; stroke-linecap: round; stroke-linejoin: round; }
  .icon-fill { fill: var(--white); }
  .tagline { fill: var(--ink-soft); font-size: 17px; letter-spacing: 4px; }
  .person-name { fill: var(--white); font-size: 25px; }
  .person-title { fill: var(--white); font-size: 17px; }
</style>
</head>
<body>
<main class="canvas">
  <section class="business-card" aria-label="Talvendrake business card">
    <svg width="900" height="514" viewBox="0 0 900 514" xmlns="http://www.w3.org/2000/svg">
      <defs>
        <linearGradient id="blue-panel-fill" x1="0" y1="1" x2="1" y2="0">
          <stop offset="0" stop-color="var(--blue-light)"/>
          <stop offset="1" stop-color="var(--blue-deep)"/>
        </linearGradient>
      </defs>

      <polygon class="blue-panel" points="900,0 900,514 333,514" fill="url(#blue-panel-fill)"/>

      <g class="brand">
        <circle class="logo-dot" cx="90" cy="210" r="40"/>
        <text class="company-name" x="148" y="226">TALVENDRAKE</text>
      </g>

      <g class="contact-block">
        <text class="address" x="120" y="300">417 Corvell West Palm Beach 33472</text>

        <g class="contact-row phone">
          <circle class="icon-bg" cx="130" cy="328" r="9"/>
          <path class="icon-glyph" d="M126.5 323.5 l2 0 1 3 -1.5 1 a6 6 0 0 0 3 3 l1 -1.5 3 1 0 2 a1.5 1.5 0 0 1 -1.5 1.5 a9 9 0 0 1 -8.5 -8.5 a1.5 1.5 0 0 1 1.5 -1.5z"/>
          <text class="contact" x="150" y="334">555.210.4471</text>
        </g>

        <g class="contact-row fax">
          <circle class="icon-bg" cx="130" cy="356" r="9"/>
          <rect class="icon-glyph" x="125" y="354" width="10" height="5"/>
          <rect class="icon-glyph" x="127" y="350.5" width="6" height="3.5"/>
          <text class="contact" x="150" y="362">555.210.4480</text>
        </g>

        <g class="contact-row email">
          <circle class="icon-bg" cx="130" cy="384" r="9"/>
          <rect class="icon-glyph" x="125" y="380.5" width="10" height="7"/>
          <path class="icon-glyph" d="M125 380.5 l5 4 5 -4"/>
          <text class="contact" x="150" y="390">marisol@talvendrake.example</text>
        </g>

        <g class="contact-row website">
          <circle class="icon-bg" cx="130" cy="412" r="9"/>
          <circle class="icon-glyph" cx="130" cy="412" r="5"/>
          <path class="icon-glyph" d="M125 412 h10 M130 407 v10"/>
          <text class="contact" x="150" y="418">www.talvendrake.example</text>
        </g>

        <text class="license" x="120" y="456">LIC.# AA00004127</text>
      </g>

      <text class="tagline" x="849" y="26" text-anchor="end" transform="rotate(-42.2 849 26)">Architecture + InteriorDesign</text>

      <g class="person">
        <text class="person-name" x="817" y="140" text-anchor="end" transform="rotate(-42.2 817 140)">Marisol Ferrant, AIA, LEED® AP</text>
        <text class="person-title" x="838" y="140" text-anchor="end" transform="rotate(-42.2 838 140)">Partner / Project Architect</text>
      </g>
    </svg>
  </section>
</main>
</body>
</html>
```